Artificial intelligence, machine learning, and automation company needs a sexy business card design

We need a sleek and sexy business card design for an AI consulting company based in Philadelphia PA. We provide custom machine learning and automation solutions for companies of all shapes and sizes. The primary industries that we serve are pharmaceuticals, engineering, healthcare, and computer software. We would like the designs to be a black business card that uses green as a sleek accent color. The final design should communicate intelligence, cutting edge new-tech, and optimization.

Target Market(s)

C-level and VP level executives of multi-million annual companies. Mostly in Pharma, Healthcare, Real Estate, Retail, and Engineering

Industry/Entity Type

Computer Software

Contact Information for Business Card

Name: Jack Moss
Title: CEO
Cell: 215 604 8293
Email: JackM@quillarcworks.example
Website: www.QuillarcWorks.example

Font styles to use
Sans Serif

Colors

Designer to choose colors to be used in the design.

Requirements
Must have
• 1) Attached Quillarc Logo (either with colors or not/embossed)
• 2) "Artificial Intelligence" "Automation" and "Machine Learning"
• 3) "Quillarc Laboratories" or "Quillarc Works" or "Quillarc"
• 4) Sexy AF.
Nice to have
• Black card / dark card color, "Quillarc Green" accent colors (in attached .ai file), Embossment of logo/name/etc, thick card stock, colored borders (on card sides, not front/back faces)
Should not have
• Should not be bland, or unsexy.

```html
<!DOCTYPE html>
<html lang="en">
<head>
<meta charset="utf-8">
<title>Quillarc Laboratories – Business Card</title>
<link href="https://fonts.googleapis.com/css2?family=Lato:wght@400;700;900&display=swap" rel="stylesheet">
<style>
  :root {
    --stage: #2c2d2e;
    --card: #4a4a4b;
    --accent: #4fc1a8;
    --ink: #ffffff;
  }
  * { box-sizing: border-box; margin: 0; padding: 0; }
  html, body { width: 1200px; height: 1000px; overflow: hidden; }
  body {
    background: var(--stage);
    font-family: "Lato", Arial, sans-serif;
    color: var(--ink);
    position: relative;
  }
  .card {
    position: absolute;
    left: 250px;
    width: 700px;
    height: 400px;
    background: var(--card);
    border-radius: 34px;
    box-shadow: 0 14px 36px rgba(0,0,0,0.45);
  }
  .card-front { top: 60px; }
  .card-back { top: 540px; }

  /* Front */
  .front-brand {
    position: absolute;
    left: 72px; top: 120px;
    display: flex; align-items: center; gap: 30px;
  }
  .brand-square {
    width: 124px; height: 124px;
    border: 7px solid var(--accent);
    flex: none;
  }
  .front-name {
    font-weight: 400;
    color: var(--ink);
    text-transform: uppercase;
    line-height: 1;
  }
  .front-name .line-main { display: block; font-size: 60px; letter-spacing: 8px; }
  .front-name .line-sub { display: block; font-size: 27px; letter-spacing: 8px; margin-top: 14px; }
  .front-services {
    position: absolute;
    left: 0; right: 0; top: 306px;
    text-align: center;
    font-size: 12px;
    font-weight: 700;
    letter-spacing: 2.5px;
    text-transform: uppercase;
    color: var(--accent);
  }

  /* Back */
  .back-brand {
    position: absolute;
    left: 75px; top: 82px;
    width: 200px;
    display: flex; flex-direction: column; align-items: center;
  }
  .back-brand .brand-square { width: 150px; height: 150px; border-width: 6px; }
  .back-name {
    margin-top: 16px;
    text-align: center;
    font-weight: 400;
    text-transform: uppercase;
    line-height: 1;
  }
  .back-name .line-main { display: block; font-size: 27px; letter-spacing: 3.5px; }
  .back-name .line-sub { display: block; font-size: 13px; letter-spacing: 3px; margin-top: 6px; }

  .divider {
    position: absolute;
    left: 310px; top: 80px;
    width: 2px; height: 240px;
    background: var(--ink);
  }
  .contact {
    position: absolute;
    left: 345px; top: 92px;
  }
  .person-name {
    font-weight: 900;
    font-size: 29px;
    color: var(--accent);
    text-transform: uppercase;
    letter-spacing: 0.5px;
  }
  .person-title {
    font-weight: 700;
    font-size: 20px;
    letter-spacing: 1px;
    margin-top: 2px;
  }
  .contact-list { list-style: none; margin-top: 16px; }
  .contact-list li {
    display: flex; align-items: center; gap: 14px;
    font-size: 19px;
    margin-bottom: 16px;
  }
  .contact-icon {
    width: 26px; height: 26px;
    border: 2px solid var(--accent);
    border-radius: 3px;
    display: flex; align-items: center; justify-content: center;
    flex: none;
  }
  .contact-icon svg { width: 16px; height: 16px; }
  .accent { color: var(--accent); }
</style>
</head>
<body>

<section class="card card-front" aria-label="Card front">
  <div class="front-brand">
    <div class="brand-square"></div>
    <p class="front-name"><span class="line-main">Quillarc</span><span class="line-sub">Laboratories</span></p>
  </div>
  <p class="front-services">Artificial Intelligence · Machine Learning · Automation</p>
</section>

<section class="card card-back" aria-label="Card back">
  <div class="back-brand">
    <div class="brand-square"></div>
    <p class="back-name"><span class="line-main">Quillarc</span><span class="line-sub">Laboratories</span></p>
  </div>

  <div class="divider"></div>

  <div class="contact">
    <h1 class="person-name">Jack Moss</h1>
    <p class="person-title">CEO</p>
    <ul class="contact-list">
      <li>
        <span class="contact-icon">
          <svg viewBox="0 0 16 16" fill="none" stroke="#4fc1a8" stroke-width="1.6">
            <path d="M4 2 L6 2 L7 5 L5.5 6.5 Q7 9.5 9.5 10.5 L11 9 L14 10 L14 12 Q14 14 12 14 Q3 13 2 4 Q2 2 4 2 Z"/>
          </svg>
        </span>
        <span>215 604 8293</span>
      </li>
      <li>
        <span class="contact-icon">
          <svg viewBox="0 0 16 16" fill="none" stroke="#4fc1a8" stroke-width="1.6">
            <rect x="1.5" y="3.5" width="13" height="9"/>
            <path d="M1.5 3.5 L8 9 L14.5 3.5"/>
          </svg>
        </span>
        <span>JackM@quillarcworks.example</span>
      </li>
      <li>
        <span class="contact-icon">
          <svg viewBox="0 0 16 16" fill="none" stroke="#4fc1a8" stroke-width="1.4">
            <circle cx="8" cy="8" r="6.2"/>
            <ellipse cx="8" cy="8" rx="2.8" ry="6.2"/>
            <path d="M1.8 8 H14.2"/>
          </svg>
        </span>
        <span>www.<span class="accent">QuillarcWorks</span>.example</span>
      </li>
    </ul>
  </div>
</section>

</body>
</html>
```